NZ First of it's kind solutions directory and marketplace for busy Mums needs a business card design

We need a business card design for our new nationwide business in NZ (long term plans to go global). We provide solutions to the everyday challenges that busy Mums face by connecting them with quality communities and suppliers of carefully selected, relevant products and services. We sell direct via our online marketplace. The final design should communicate our values of inclusivity, quality and smart solutions. Colours should incorporate our logo colour palette of #477077 and #6ba8b2. Our website is at https://www.brightnestly.com

Target Market(s)

busy Mums, Age 28 – 50, female, income over $100K, location main centres NZ primarily but NZ wide. Is likely juggling work or career with a young family. Probably had hobbies which have fallen by the wayside.
-Wants to succeed in her chosen career without compromising on family life
-to successfully juggle her career without feeling like she is compromising her children
- Is time poor, something always has to give and it’s generally her health (she’ll stay up late, get stressed)
- probably ex corporate or professional career. Has discretional income

Industry/Entity Type

Business

Contact Information for Business Card

Jodie Farnsworth, Founder, BrightNestly.com (Strapline Browse; Pick; Sorted), 48 Kowhai Terrace, Hillsborough, Auckland 1058, New Zealand. Mob: 021 437 518 Ph: +64 (0)9 584 7163

Font styles to use
Other font styles liked:
• Raleway, and/or Architects Daughter

Colors
00a990
33b8a4
86cfc6
cfeae6

Requirements
Must have
• the above details, streamline. the logo and colours associated with those logos
Should not have
• foil or metallic colours

```html
<!DOCTYPE html>
<html lang="en">
<head>
<meta charset="utf-8">
<title>BrightNestly business card concepts</title>
<link rel="stylesheet" href="https://fonts.googleapis.com/css2?family=Raleway:wght@400;500;700;800&display=swap">
<style>
  :root {
    --page: #f8f9fa;
    --mint: #87cfc6;
    --deep: #477077;
    --teal: #6ba8b2;
    --ink: #2f3b3d;
    --label: #555b5d;
    --ghost: #eceff0;
    --white: #ffffff;
  }
  * { box-sizing: border-box; margin: 0; padding: 0; }
  html, body { width: 1200px; height: 1200px; overflow: hidden; }
  body {
    background: var(--page);
    font-family: "Raleway", Arial, sans-serif;
    position: relative;
  }
  .concept-label {
    position: absolute;
    left: 43px;
    font-size: 14.5px;
    color: var(--label);
    font-weight: 400;
  }
  .card {
    position: absolute;
    width: 400px;
    height: 228px;
    overflow: hidden;
    box-shadow: 0 6px 12px rgba(0,0,0,0.12);
  }
  .card-front { background: var(--mint); color: var(--white); }
  .card-back { background: var(--white); }

  .brand-mark {
    display: inline-block;
    border-radius: 50%;
    background: var(--white);
  }
  .brand-name {
    font-weight: 800;
    letter-spacing: -0.5px;
    line-height: 1;
  }
  .site-url {
    font-size: 16px;
    font-weight: 400;
    line-height: 1;
    white-space: nowrap;
  }

  /* Concept 1 front */
  .front-one .brand-row {
    position: absolute; left: 22px; top: 158px;
    display: flex; align-items: center; gap: 10px;
    height: 30px;
  }
  .front-one .brand-mark { width: 26px; height: 26px; flex: none; }
  .front-one .brand-name { font-size: 28px; }
  .front-one .site-url { position: absolute; left: 59px; top: 193px; }

  /* Concept 2 front */
  .front-two { text-align: center; }
  .front-two .brand-mark { position: absolute; left: 186px; top: 70px; width: 28px; height: 28px; }
  .front-two .brand-name { position: absolute; left: 0; right: 0; top: 116px; font-size: 28px; }
  .front-two .site-url { position: absolute; left: 0; right: 0; top: 151px; }

  /* Backs */
  .holder { position: absolute; left: 14px; top: 26px; }
  .holder-name { font-size: 21px; font-weight: 700; color: var(--deep); line-height: 1.05; letter-spacing: 0.2px; }
  .holder-role { font-size: 14.5px; font-weight: 500; color: var(--teal); line-height: 1.1; margin-left: 2px; }
  .back-brand {
    position: absolute; right: 15px; top: 36px;
    font-size: 22px; font-weight: 800; color: var(--deep);
    letter-spacing: -0.4px; line-height: 1;
  }
  .contact-list { position: absolute; left: 20px; list-style: none; z-index: 1; }
  .contact-list li {
    display: flex; align-items: flex-start; gap: 8px;
    font-size: 14.5px; color: var(--ink); line-height: 18px;
    margin-bottom: 3px;
    white-space: nowrap;
  }
  .contact-list li.address { margin-top: 5px; }
  .contact-list svg { width: 10px; height: 12px; margin-top: 3px; flex: none; fill: none; stroke: var(--teal); stroke-width: 1.2; }
  .back-one .contact-list { top: 114px; }
  .back-two .contact-list { top: 114px; }
  .ghost-disc {
    position: absolute; left: 262px; top: 70px;
    width: 210px; height: 210px; border-radius: 50%;
    background: var(--ghost);
  }
</style>
</head>
<body>

<svg width="0" height="0" style="position:absolute" aria-hidden="true">
  <defs>
    <symbol id="icon-phone" viewBox="0 0 10 12"><path d="M2 1 L4 3.5 L3 5 Q4.5 8 6.5 9 L8 8 L9.5 10.5 Q8 12 6 11 Q2 8.5 1 3.5 Q1 2 2 1 Z"/></symbol>
    <symbol id="icon-mobile" viewBox="0 0 10 12"><rect x="2" y="1" width="6" height="10" rx="1"/></symbol>
    <symbol id="icon-link" viewBox="0 0 10 12"><path d="M4.5 4.5 L6.5 2.5 Q8 1 9 2.5 Q10 4 8.5 5 L6.5 7 M5.5 7.5 L3.5 9.5 Q2 11 1 9.5 Q0 8 1.5 7 L3.5 5 M3.5 8.5 L6.5 3.5"/></symbol>
    <symbol id="icon-pin" viewBox="0 0 10 12"><path d="M5 11 Q1 6.5 1 4.5 A4 4 0 0 1 9 4.5 Q9 6.5 5 11 Z"/><circle cx="5" cy="4.5" r="1.4"/></symbol>
  </defs>
</svg>

<p class="concept-label" style="top:340px">Concept 1</p>

<section class="card card-front front-one" style="left:144px; top:235px">
  <div class="brand-row">
    <span class="brand-mark"></span>
    <span class="brand-name">BrightNestly</span>
  </div>
  <p class="site-url">www.brightnestly.com</p>
</section>

<section class="card card-back back-one" style="left:656px; top:234px">
  <div class="holder">
    <p class="holder-name">Jodie Farnsworth</p>
    <p class="holder-role">Founder</p>
  </div>
  <p class="back-brand">BrightNestly</p>
  <ul class="contact-list">
    <li><svg><use href="#icon-phone"/></svg>+64 (0)9 584 7163</li>
    <li><svg><use href="#icon-mobile"/></svg>021 437 518</li>
    <li><svg><use href="#icon-link"/></svg>www.brightnestly.com</li>
    <li class="address"><svg><use href="#icon-pin"/></svg><span>48 Kowhai Terrace, Hillsborough, Auckland 1058,<br>New Zealand</span></li>
  </ul>
</section>

<p class="concept-label" style="top:766px">Concept 2</p>

<section class="card card-front front-two" style="left:144px; top:662px">
  <span class="brand-mark"></span>
  <p class="brand-name">BrightNestly</p>
  <p class="site-url">www.brightnestly.com</p>
</section>

<section class="card card-back back-two" style="left:656px; top:662px">
  <div class="ghost-disc"></div>
  <div class="holder">
    <p class="holder-name">Jodie Farnsworth</p>
    <p class="holder-role">Founder</p>
  </div>
  <p class="back-brand">BrightNestly</p>
  <ul class="contact-list">
    <li><svg><use href="#icon-phone"/></svg>+64 (0)9 584 7163</li>
    <li><svg><use href="#icon-mobile"/></svg>021 437 518</li>
    <li><svg><use href="#icon-link"/></svg>www.brightnestly.com</li>
    <li class="address"><svg><use href="#icon-pin"/></svg><span>48 Kowhai Terrace, Hillsborough,<br>Auckland 1058, New Zealand</span></li>
  </ul>
</section>

</body>
</html>
```